BWH Business Card Design

We are a small construction equipment rental and hardware store located in Middle Tennessee. We have three stores. Our primary business is construction equipment. We have an existing logo we'd like to use. I think I would like to list each store physical address on the back of the card and maybe the web address also: www.bwhrentco.example.

We also need a design that we can incorporate into company letterhead, small note pads, and even checks if possible.

Industry/Entity Type

Construction

Contact Information for Business Card

We have our Logo, Name: Bramwell Hoisting Works, Employee Name, Main Phone Number, Mobile Phone Number, Email Address, Company Address, and website information (There are three locations that can go on the back if necessary) We would like to leave some room on the back of the card in case we want to write information down on it.

```html
<!DOCTYPE html>
<html lang="en">
<head>
<meta charset="utf-8">
<title>BWH Business Card</title>
<link href="https://fonts.googleapis.com/css2?family=Open+Sans:wght@400;600;700&display=swap" rel="stylesheet">
<style>
  :root {
    --page: #e9e6e1;
    --navy: #2a3a8f;
    --navy-deep: #1f2c78;
    --navy-light: #3a4fa8;
    --red: #e0384d;
    --paper: #f7f7f7;
    --grey-text: #9a9ea8;
    --white: #ffffff;
  }
  * { margin: 0; padding: 0; box-sizing: border-box; }
  html, body { width: 1200px; height: 858px; overflow: hidden; }
  body {
    background: var(--page);
    font-family: "Open Sans", Arial, sans-serif;
    display: flex; align-items: center; justify-content: center; gap: 40px;
  }
  .card {
    position: relative; width: 560px; height: 320px; overflow: hidden;
    border-radius: 4px; box-shadow: 0 6px 18px rgba(0,0,0,.18);
  }
  .card-front { background: var(--paper); }
  .front-shape { position: absolute; inset: 0; }
  .brand {
    position: absolute; left: 34px; top: 96px; width: 220px;
    display: flex; flex-direction: column; align-items: center; gap: 14px;
  }
  .brand-dot { width: 74px; height: 74px; border-radius: 50%; background: var(--navy-light); }
  .brand-name {
    color: var(--grey-text); font-weight: 700; font-size: 17px;
    text-transform: uppercase; text-align: center; line-height: 1.15;
  }
  .contact {
    position: absolute; left: 318px; top: 40px; color: var(--white);
  }
  .contact-city { font-size: 28px; font-weight: 600; margin-bottom: 14px; }
  .contact-address { font-size: 13px; line-height: 1.45; margin-bottom: 14px; }
  .contact-list { list-style: none; font-size: 14px; line-height: 1.6; }
  .contact-list li { display: flex; align-items: center; gap: 9px; }
  .contact-list svg { width: 13px; height: 13px; flex: none; }
  .card-back {
    background: radial-gradient(circle at 45% 25%, var(--navy-light), var(--navy-deep) 80%);
    color: var(--white);
  }
  .back-title {
    position: absolute; left: 0; right: 0; top: 92px; text-align: center;
    font-weight: 700; font-size: 34px; line-height: 1.15; text-transform: uppercase;
  }
  .back-rule {
    position: absolute; left: 30px; right: 30px; top: 232px;
    display: flex; align-items: center; gap: 14px; font-size: 15px;
  }
  .back-rule::before, .back-rule::after {
    content: ""; flex: 1; height: 1px; background: var(--white);
  }
  .back-rule::before { flex: .3; }
</style>
</head>
<body>
  <section class="card card-front">
    <svg class="front-shape" viewBox="0 0 560 320" preserveAspectRatio="none" aria-hidden="true">
      <defs>
        <linearGradient id="navyFill" x1="0" y1="0" x2="1" y2="1">
          <stop offset="0" stop-color="#3a4fa8"/>
          <stop offset="1" stop-color="#1f2c78"/>
        </linearGradient>
      </defs>
      <path d="M220 0 Q330 150 300 320 L280 320 Q312 150 200 0 Z" fill="#e0384d"/>
      <path d="M228 0 Q338 150 308 320 L560 320 L560 0 Z" fill="url(#navyFill)"/>
    </svg>
    <div class="brand">
      <span class="brand-dot"></span>
      <p class="brand-name">Bramwell Hoisting<br>Works</p>
    </div>
    <div class="contact">
      <h1 class="contact-city">Nashville</h1>
      <p class="contact-address">Your Address 2nd Lane<br>Ave Franklin, TN 00000</p>
      <ul class="contact-list">
        <li><svg viewBox="0 0 12 12"><rect x="1" y="1" width="10" height="10" rx="2" fill="none" stroke="#e0384d" stroke-width="2"/></svg>XXX XXX XXXX</li>
        <li><svg viewBox="0 0 12 12"><rect x="1" y="3" width="10" height="8" rx="1" fill="#e0384d"/><rect x="3" y="1" width="6" height="3" fill="#e0384d"/></svg>XXX XXX XXXX</li>
        <li><svg viewBox="0 0 12 12"><circle cx="6" cy="6" r="5" fill="#e0384d"/><path d="M1 6h10M6 1v10" stroke="#2a3a8f" stroke-width="1"/></svg>www.bwhrentco.example</li>
        <li><svg viewBox="0 0 12 12"><rect x="0.5" y="2" width="11" height="8" fill="#e0384d"/><path d="M1 2.5l5 4 5-4" fill="none" stroke="#fff" stroke-width="1"/></svg>info@bwhrentco.example</li>
      </ul>
    </div>
  </section>

  <section class="card card-back">
    <h2 class="back-title">Bramwell Hoisting<br>Works</h2>
    <p class="back-rule">www.bwhrentco.example</p>
  </section>
</body>
</html>
```